A UK based Lettings and Property Management Company - Brindle Oak Property

Brindle Oak Property rents and manages properties on behalf of owners in Liverpool, UK. We are looking for a clean, fresh modern design which incororates our logo.

In terms of pages we initially require:

Home
Lettings
Property Management
Landlords
Tenants
About
Contact

In would like to use colours compatible with the logo

Target Market(s)

People looking to rent property
Owners looking to use our services to let their property

Industry/Entity Type

Property

Contact Information for Business Card

Logo prominent on one side
Address to be edited by us as we are moving premises in October
Name Gareth Whitlow
Tel number 0151 486 2037
e-mail gareth@brindleoakhomes.co.uk

Font styles to use
Sans Serif

Colors

Designer to choose colors to be used in the design.

Requirements
Must have
• Clean lines
• Fresh
• Easy navigation
• Easy editing
• Data capture

```html
<!DOCTYPE html>
<html lang="en">
<head>
<meta charset="UTF-8">
<title>Brindle Oak Property</title>
<link href="https://fonts.googleapis.com/css2?family=Poppins:wght@300;400;500;600;700&display=swap" rel="stylesheet">
<style>
:root{
  --navy:#12133f;
  --navy-panel:rgba(26,28,88,.95);
  --band:#2b3273;
  --ink:#1b1c2e;
  --muted:#6b6e7a;
  --soft-bg:#f3f6fb;
  --white:#ffffff;
}
*{margin:0;padding:0;box-sizing:border-box}
html,body{width:1200px;height:1200px;overflow:hidden}
body{font-family:'Poppins',sans-serif;background:var(--white);color:var(--ink);position:relative}
.abs{position:absolute}

.topbar{left:0;top:0;width:1200px;height:36px;background:var(--navy);color:var(--white);font-size:11px}
.topbar span{position:absolute;top:11px}
.topbar .sep{left:304px;top:11px;width:1px;height:13px;background:#5a5da0}
.topbar .caret{display:inline-block;border:4px solid transparent;border-top:5px solid #fff;border-bottom:0;margin-left:5px;vertical-align:2px}

.header{left:0;top:36px;width:1200px;height:86px;background:var(--white)}
.logo{left:132px;top:22px;display:flex;align-items:center;gap:9px}
.logo .mark{width:34px;height:34px;background:var(--navy)}
.logo .name{color:var(--navy);font-weight:600;font-size:17px;line-height:18px;letter-spacing:.5px}
.nav{left:434px;top:33px;display:flex;gap:0;font-size:12px;font-weight:500;color:var(--ink)}
.nav a{color:inherit;text-decoration:none;margin-right:29.5px}
.nav a:last-child{margin-right:0}

.hero{left:0;top:122px;width:1200px;height:456px;background:linear-gradient(100deg,#e9c9b4 0%,#d9b199 35%,#9a7e78 60%,#5c6a9a 75%,#8a6a5a 100%)}
.hero-panel{left:132px;top:233px;width:464px;height:234px;background:var(--navy-panel);color:var(--white)}
.hero-panel .kicker{position:absolute;left:27px;top:27px;font-size:16px;font-weight:300}
.hero-panel .dash{position:absolute;top:57px;height:3px;background:var(--white)}
.hero-panel h1{position:absolute;left:27px;top:77px;font-size:28px;line-height:36px;font-weight:700;letter-spacing:-.3px}
.btn{display:flex;align-items:center;justify-content:center;background:var(--white);color:var(--navy);font-size:12px;font-weight:500;width:128px;height:39px}
.hero-panel .btn{position:absolute;left:30px;top:164px}

.welcome{left:0;top:578px;width:1200px;height:434px;background:var(--soft-bg)}
.welcome h2{position:absolute;left:119px;top:40px;font-size:26px;font-weight:700;letter-spacing:1px;color:var(--ink);line-height:32px}
.welcome h2 .hl{background:var(--navy);color:var(--white);padding:0 4px}
.welcome .sub{position:absolute;left:122px;top:79px;font-size:17px;color:var(--navy)}
.welcome .intro{position:absolute;left:120px;top:122px;width:540px;font-size:12px;line-height:21px;color:var(--muted)}
.feature{position:absolute;width:220px}
.feature svg{position:absolute;left:0;top:0}
.feature h3{position:absolute;left:35px;top:0;font-size:12.5px;font-weight:600;white-space:nowrap}
.feature p{position:absolute;left:35px;top:24px;font-size:11.5px;line-height:18px;color:var(--muted);white-space:nowrap}
.house{left:672px;top:620px;width:420px;height:345px;background:radial-gradient(ellipse at 50% 45%,#e6e9ef 0%,#eef1f6 50%,var(--soft-bg) 75%)}

.signup{left:0;top:1012px;width:1200px;height:109px;background:linear-gradient(90deg,#2a3070,#333b7e 50%,#2a3070)}
.signup p{position:absolute;left:131px;top:41px;font-size:20px;font-weight:700;color:var(--white);letter-spacing:.6px}
.signup .btn{position:absolute;left:939px;top:35px}

.featured h2{position:absolute;left:131px;top:1153px;font-size:26px;font-weight:700;letter-spacing:1px}
.arrow{top:1152px;width:32px;height:31px;background:var(--navy);display:flex;align-items:center;justify-content:center}
</style>
</head>
<body>

<div class="abs topbar">
  <span style="left:131px">Need Support ? 0151 486 2037</span>
  <div class="abs sep"></div>
  <span style="left:319px">Mail Us : www.brindleoakproperty.co.uk</span>
  <span style="left:909px">ENG<i class="caret"></i></span>
  <span style="left:961px">LOGIN</span>
  <span style="left:1022px">REGISTER</span>
</div>

<header class="abs header">
  <div class="abs logo"><div class="mark"></div><div class="name">BRINDLE OAK<br>PROPERTY</div></div>
  <nav class="abs nav">
    <a href="#">HOME</a><a href="#">LETTINGS</a><a href="#">PROPERTY MANAGEMENT</a><a href="#">LANDLORDS</a><a href="#">TENANTS</a><a href="#">ABOUT</a><a href="#">CONTACT US</a>
  </nav>
</header>

<section class="abs hero" role="img" aria-label="Photo of a smiling family with a baby lying on a rug at home"></section>
<div class="abs hero-panel">
  <div class="kicker">WANT TO BUY OR SELL HOME ?</div>
  <div class="dash" style="left:29px;width:10px"></div>
  <div class="dash" style="left:44px;width:34px"></div>
  <h1>WE WILL HELP YOU TO SOLVE<br>YOUR PROBLEM</h1>
  <a class="btn">CONTACT US</a>
</div>

<section class="abs welcome">
  <h2>WELCOME TO BRINDLE <span class="hl">OAK</span></h2>
  <div class="sub">We always provide prority to our customer</div>
  <p class="intro">Harrow|Bent Investment Real Estate (HB) is committed to excellence. Our offices are located in Manhattan Beach, Santa Monica, and Long Beach. Our investment team consists of dedicated, results-driven brokers, marketing specialists, agents and coordinators, all backed by the most innovative and scalable technology the commercial real estate industry has to offer.</p>

  <div class="feature" style="left:119px;top:234px">
    <svg width="24" height="26" viewBox="0 0 24 26" fill="none" stroke="#333" stroke-width="1.2"><circle cx="9" cy="17" r="7"/><path d="M6 8l3-5 3 5M9 10v6"/><ellipse cx="18" cy="21" rx="5" ry="2"/><ellipse cx="18" cy="18" rx="5" ry="2"/></svg>
    <h3>LOW COST</h3><p>One of the more obscure<br>Latin words, consectetur,</p>
  </div>
  <div class="feature" style="left:365px;top:234px">
    <svg width="26" height="26" viewBox="0 0 26 26" fill="none" stroke="#333" stroke-width="1.2"><path d="M2 16l6-6 5 4 9-10M18 4h4v4"/><path d="M3 25v-4M7 25v-6M11 25v-5M15 25v-7M19 25v-9M23 25v-11"/></svg>
    <h3>GOOD MARKETING</h3><p>One of the more obscure<br>Latin words, consectetur,</p>
  </div>
  <div class="feature" style="left:119px;top:322px">
    <svg width="26" height="26" viewBox="0 0 26 26" fill="none" stroke="#333" stroke-width="1.3"><circle cx="16" cy="10" r="8"/><path d="M10 16L2 24"/></svg>
    <h3>EASY TO FIND</h3><p>One of the more obscure<br>Latin words, consectetur,</p>
  </div>
  <div class="feature" style="left:365px;top:322px">
    <svg width="24" height="26" viewBox="0 0 24 26" fill="none" stroke="#333" stroke-width="1.2"><path d="M12 2l9 3v8c0 6-4 9-9 11-5-2-9-5-9-11V5z"/><circle cx="12" cy="13" r="5"/><path d="M12 9v8M14 11h-3a1 1 0 000 2h2a1 1 0 010 2h-3"/></svg>
    <h3>RELIABLE</h3><p>One of the more obscure<br>Latin words, consectetur,</p>
  </div>
</section>
<div class="abs house" role="img" aria-label="Sketched architectural drawing of a house above its floor plan"></div>

<section class="abs signup" role="region" aria-label="Sign up">
  <p>SIGN UP NOW AND GET NOTIFICATION FOR NEW PROPERTIES!!!</p>
  <a class="btn">SIGN UP NOW</a>
</section>

<section class="featured">
  <h2>FEATURED PROPERTY</h2>
  <div class="abs arrow" style="left:1000px"><svg width="10" height="12" viewBox="0 0 10 12" fill="none" stroke="#fff" stroke-width="1.5"><path d="M7 1L2 6l5 5"/></svg></div>
  <div class="abs arrow" style="left:1036px"><svg width="10" height="12" viewBox="0 0 10 12" fill="none" stroke="#fff" stroke-width="1.5"><path d="M3 1l5 5-5 5"/></svg></div>
</section>

</body>
</html>
```